Web Design Project - CCTV in Terravue Charts

I need a Design for a SAAS website.

The company is a B2B R&D company developing live CCTV video that's monitored on terravue charts & velmora globe.

We need a simple, calm & uncluttered design.
The site will be used for A/B testing of our products features.

The initial design will deal with the website.

Five Main Pages
Home
Products
DEMO - SAAS (selected designer to finalize)
Register
Generic Page

The generic page will be used for everything else, such as About us, Latest News, Contact us (same as register), support etc.

I have included a few mock ups just to give an idea of my initial thoughts on shapes, colours and simplicity of design, using Terravue Charts as a background. Each page or news article may have it's own geolocation, can this can be reflected in the design.

I would like this to all work in a Joomla type CMS so it can be easily updated and for A/B testing landing pages.(please advise me on the best system)

The second component to the website will be the SAAS administration area. We have the functional techie bit sorted but the design needs to fit branding.
This part of the project will be discussed with the designer upon selection of the most suitable design. We are hoping the designer will help with the look and feel of the administration section.

Many thanks for looking at this Project. Please contact me if if you need more information.

Logo & Logo Colour is indicatives only .

PS.
The following sites for their simplicity.
https://www.stashquill.com/home
I love the fact that its all about the product, not them.

http://www.valtremorides.com/en
This is the site that inspired the website idea.

It Company

• Terravue Chart Background
Greyed Out Terravue Chart background

```html
<!DOCTYPE html>
<html lang="en">
<head>
<meta charset="utf-8">
<title>Sentra Terrain – Home</title>
<link rel="stylesheet" href="https://fonts.googleapis.com/css2?family=Source+Sans+3:wght@400;600&display=swap">
<style>
  :root {
    --teal: #17809a;
    --teal-light: #36b3cf;
    --teal-dark: #0b6a82;
    --ink: #2b2b2b;
    --body-text: #444444;
    --muted: #6b6b6b;
    --map-light: #efefef;
    --map-mid: #dcdcdc;
    --panel-border: #6f6f6f;
    --rule-blue: #2d9ac0;
    --button-dark: #2f2f2f;
    --white: #ffffff;
  }
  * { box-sizing: border-box; margin: 0; padding: 0; }
  html, body { width: 1200px; height: 980px; overflow: hidden; }
  body {
    position: relative;
    background: var(--white);
    font-family: "Source Sans 3", "Helvetica Neue", Arial, sans-serif;
    color: var(--ink);
  }
  .map-backdrop {
    position: absolute; left: 0; top: 78px; width: 1200px; height: 760px;
    background: radial-gradient(ellipse at 30% 40%, var(--map-light), var(--map-mid) 70%, #e6e6e6);
    border-bottom: 2px solid var(--rule-blue);
  }
  .site-header {
    position: absolute; left: 0; top: 0; width: 1200px; height: 78px;
    background: linear-gradient(#ffffff, #f1f1f1);
    border-bottom: 1px solid #cfcfcf;
    box-shadow: 0 1px 3px rgba(0,0,0,.12);
    z-index: 2;
  }
  .brand {
    position: absolute; left: 135px; top: 24px;
    display: flex; align-items: center; gap: 8px;
    font-size: 23px; color: var(--ink); font-weight: 400;
  }
  .brand-mark { width: 28px; height: 28px; border-radius: 50%; background: var(--teal); }
  .main-nav a {
    position: absolute; top: 22px; height: 37px; line-height: 37px; font-size: 16.5px;
    color: var(--ink); text-decoration: none; white-space: nowrap;
  }
  .main-nav .nav-home {
    left: 551px; width: 82px; text-align: center; border-radius: 18px; color: var(--white);
    background: linear-gradient(var(--teal-light), var(--teal-dark));
    border: 1px solid var(--teal-dark);
  }
  .main-nav .nav-products { left: 669px; top: 23px; }
  .main-nav .nav-demo { left: 780px; }
  .main-nav .nav-register { left: 881px; }
  .main-nav .nav-contact { left: 993px; }
  .hero {
    position: absolute; left: 131px; top: 94px; width: 938px; height: 414px;
    border: 3px solid var(--white); border-radius: 12px; overflow: hidden;
    background: #000;
    box-shadow: 0 2px 6px rgba(0,0,0,.35);
  }
  .hero-globe {
    position: absolute; inset: 0;
    background: radial-gradient(circle 600px at 230px 500px,
      #7f8a5c 0%, #4f8a6a 22%, #2f78b8 48%, #1f64a6 66%, #0d3a6e 80%, #03101f 90%, #000 96%);
  }
  .hero-title {
    position: absolute; left: 528px; top: 152px; z-index: 1;
    font-size: 44px; line-height: 52px; font-weight: 400; color: var(--white);
    letter-spacing: .6px;
  }
  .features {
    position: absolute; left: 131px; top: 534px; width: 938px; height: 341px;
    background: var(--white); border: 2px solid var(--panel-border); border-radius: 12px;
    box-shadow: 0 1px 4px rgba(0,0,0,.2);
  }
  .feature { position: absolute; top: 20px; width: 280px; }
  .feature-one { left: 20px; }
  .feature-two { left: 332px; }
  .feature-three { left: 643px; }
  .feature-title { font-size: 25px; font-weight: 400; color: var(--teal); line-height: 30px; }
  .feature-art { margin-top: 12px; height: 112px; border-radius: 6px; }
  .art-computer { width: 180px; margin-left: 14px; background: linear-gradient(135deg, #3a3a3a, #3fa7e0 55%, #5ea24b); }
  .art-map { width: 170px; margin-left: 22px; background: linear-gradient(135deg, #d8ecf8, #6fb3e6 60%, #d23b2a); }
  .art-phones { width: 218px; background: linear-gradient(90deg, #222, #9bbd8e 30%, #222 50%, #9bbd8e 80%, #222); }
  .feature-text { margin-top: 16px; width: 270px; font-size: 14px; line-height: 20px; color: var(--body-text); }
  .more-button {
    position: absolute; top: 274px; width: 64px; height: 30px; line-height: 30px;
    text-align: center; font-size: 15px; font-weight: 600; color: var(--white);
    background: linear-gradient(#4a4a4a, var(--button-dark)); border-radius: 2px; text-decoration: none;
  }
  .more-one { left: 21px; }
  .more-two { left: 333px; }
  .more-three { left: 644px; }
  .site-footer {
    position: absolute; left: 131px; top: 913px; width: 934px; height: 22px;
    font-size: 13px; color: var(--muted);
  }
  .legal { position: absolute; left: 0; top: 2px; }
  .legal span { margin: 0 6px; }
  .share-button, .share-count {
    position: absolute; top: 0; height: 21px; line-height: 19px; text-align: center;
    font-size: 12px; color: #333; border-radius: 3px;
  }
  .share-button { border: 1px solid #b9c3d3; background: linear-gradient(#f7f9fc, #e3e8f0); }
  .share-count { border: 1px solid #cfcfcf; background: var(--white); }
  .like { left: 685px; width: 45px; }
  .like-count { left: 735px; width: 22px; }
  .tweet { left: 768px; width: 59px; }
  .tweet-count { left: 831px; width: 26px; }
  .plus { left: 869px; width: 32px; }
  .plus-count { left: 905px; width: 29px; }
</style>
</head>
<body>
  <div class="map-backdrop" role="img" aria-label="Greyed-out street map background"></div>

  <header class="site-header">
    <div class="brand"><span class="brand-mark"></span>Sentra Terrain</div>
    <nav class="main-nav">
      <a class="nav-home" href="#">Home</a>
      <a class="nav-products" href="#">Products</a>
      <a class="nav-demo" href="#">Demo</a>
      <a class="nav-register" href="#">Register</a>
      <a class="nav-contact" href="#">Contact Us</a>
    </nav>
  </header>

  <section class="hero">
    <div class="hero-globe" role="img" aria-label="Planet Earth seen from space against a starfield"></div>
    <h1 class="hero-title">Connect with<br>Your Assests Online!</h1>
  </section>

  <section class="features">
    <article class="feature feature-one">
      <h2 class="feature-title">Create Global Assets</h2>
      <div class="feature-art art-computer" role="img" aria-label="Desktop computer with globe and gear icon"></div>
      <p class="feature-text">Create an online library of all your physical assets live and status reports inside of velmora globe.</p>
    </article>
    <article class="feature feature-two">
      <h2 class="feature-title">Olympic Scalability</h2>
      <div class="feature-art art-map" role="img" aria-label="Folded world map with a red location pin"></div>
      <p class="feature-text">Supporting 1000s of simulaiouns live video feed and alarms sentra terrain. Starts small and scale to any size projects.</p>
    </article>
    <article class="feature feature-three">
      <h2 class="feature-title">Made to Touch</h2>
      <div class="feature-art art-phones" role="img" aria-label="Three smartphones showing maps"></div>
      <p class="feature-text">Sentra terrain loves to be touch, it works on any devices either lives or offline for when its really of the grid.</p>
    </article>
    <a class="more-button more-one" href="#">more</a>
    <a class="more-button more-two" href="#">more</a>
    <a class="more-button more-three" href="#">more</a>
  </section>

  <footer class="site-footer">
    <div class="legal">2012 © Orvanta<span>|</span>Privacy Policy<span>|</span>Terms of Service</div>
    <span class="share-button like">Like</span><span class="share-count like-count">3k</span>
    <span class="share-button tweet">Tweet</span><span class="share-count tweet-count">316</span>
    <span class="share-button plus">+1</span><span class="share-count plus-count">81</span>
  </footer>
</body>
</html>
```